Harbor Business Cards

I need a business card designed with the following information.

Company Name: Harbor Wealth Management
Name: BriAnne Dockery
Title: Executive Assistant
Cell: (555) 555-0173
Direct Line: (555) 555-0148
Email: brianne@harborwmx.com
Address: 20537 W. Marlowe PKWY Ste. B
Fernvale, NV 77390

I have attached the logo.
I would like it in navy blue and silver.
Thanks.

```html
<!DOCTYPE html>
<html lang="en">
<head>
<meta charset="utf-8">
<title>Harbor Wealth Management – Business Card</title>
<link rel="stylesheet" href="https://fonts.googleapis.com/css2?family=Goudy+Bookletter+1911&display=swap">
<style>
  :root {
    --navy: #0c2140;
    --silver: #bcc5cc;
    --stage: #070605;
  }
  * { margin: 0; padding: 0; box-sizing: border-box; }
  html, body { width: 1200px; height: 1200px; overflow: hidden; background: var(--stage); }
  body { position: relative; font-family: "Goudy Bookletter 1911", Georgia, serif; }

  .card { position: absolute; }

  /* Front */
  .card-front { left: 181px; top: 133px; width: 861px; height: 420px; background: var(--silver); }
  .stripe { position: absolute; top: 0; height: 100%; background: var(--navy); }
  .stripe-a { left: 26px; width: 31px; }
  .stripe-b { left: 87px; width: 30px; }
  .stripe-c { right: 0; width: 30px; }
  .front-brand {
    position: absolute; left: 131px; width: 660px; top: 272px;
    text-align: center; color: var(--navy); text-transform: uppercase;
  }
  .front-brand .brand-name { display: block; font-size: 54px; line-height: 60px; letter-spacing: 0.42em; padding-left: 0.42em; }
  .front-brand .brand-sub { display: block; font-size: 22px; line-height: 28px; margin-top: 8px; letter-spacing: 0.26em; padding-left: 0.26em; }

  /* Back */
  .card-back { left: 183px; top: 670px; width: 862px; height: 401px; background: var(--silver); }
  .back-panel { position: absolute; left: 15px; top: 16px; width: 831px; height: 369px; background: var(--navy); color: var(--silver); }
  .identity { position: absolute; left: 0; width: 412px; top: 14px; text-align: center; }
  .person-name { font-size: 56px; line-height: 1.1; font-weight: 400; }
  .person-title { font-size: 38px; line-height: 1.2; margin-top: 4px; font-weight: 400; }
  .back-brand {
    position: absolute; left: 0; width: 412px; top: 284px; text-align: center; text-transform: uppercase;
  }
  .back-brand .brand-name { display: block; font-size: 34px; line-height: 38px; letter-spacing: 0.45em; padding-left: 0.45em; }
  .back-brand .brand-sub { display: block; font-size: 14px; line-height: 18px; margin-top: 6px; letter-spacing: 0.28em; padding-left: 0.28em; }
  .bar { position: absolute; background: var(--silver); }
  .bar-1 { left: 424px; top: 15px; width: 16px; height: 291px; }
  .bar-2 { left: 459px; top: 36px; width: 14px; height: 296px; }
  .bar-3 { left: 492px; top: 82px; width: 15px; height: 276px; }
  .contact { position: absolute; left: 524px; top: 22px; font-size: 25px; line-height: 30px; white-space: nowrap; }
  .contact p + p { margin-top: 30px; }
</style>
</head>
<body>
  <section class="card card-front" aria-label="Card front">
    <div class="stripe stripe-a"></div>
    <div class="stripe stripe-b"></div>
    <div class="stripe stripe-c"></div>
    <div class="front-brand">
      <span class="brand-name">Harbor</span>
      <span class="brand-sub">Wealth Management</span>
    </div>
  </section>

  <section class="card card-back" aria-label="Card back">
    <div class="back-panel">
      <div class="identity">
        <h1 class="person-name">BriAnne Dockery</h1>
        <h2 class="person-title">Executive Assistant</h2>
      </div>
      <div class="back-brand">
        <span class="brand-name">Harbor</span>
        <span class="brand-sub">Wealth Management</span>
      </div>
      <div class="bar bar-1"></div>
      <div class="bar bar-2"></div>
      <div class="bar bar-3"></div>
      <div class="contact">
        <p>Cell: (555) 555-0173</p>
        <p>Direct Line:<br>(555) 555-0148</p>
        <p>Email:<br>brianne@harborwmx.com</p>
        <p>Address: 20537 W.<br>Marlowe PKWY Ste. B<br>Fernvale, NV 77390</p>
      </div>
    </div>
  </section>
</body>
</html>
```